New Website for Asia Travel Agency

Lanternpath Journeys Website

We want a redesign for our current website, www.lanternpathjourneys.example. We want you to get creative with our brand and present our company in a unique, creative and compelling way, that communicates our exotic destinations and tours, the local and authentic character of our travel consultants and the trustworthy and professional nature of our company.

Who is this company?

Lanternpath Journeys is an online tour operator specializing in providing tailor-made tours to eight destinations in Asia; Vietnam, Thailand, Laos, Cambodia, Indonesia, Myanmar, Japan and China. They were launched in mid February 2012 with headquarters in Bangkok, Thailand, and staffed by locals and expats with many years of experience in the travel industry, and who are committed to sharing their deep knowledge of, and passion for the region.

Local knowledge

Our consultants at Lanternpath Journeys are all locals – they know their destinations inside-out and draw upon invaluable first-hand experience and information when planning your tour. They have insights into local culture and tradition, they know the best places to visit, the most worthwhile experiences to have and, most importantly, they have the knowledge to create exactly the holiday you desire.

All hotels and activities featured in a Lanternpath Journeys tour are regularly inspected by our consultants to ensure the highest quality standards are met and that all information is correct and up to date.

Unforgettable Travel Experiences

Whether it's a cultural exploration or a beach holiday you're after – or a mix of both – Lanternpath Journeys has an itinerary for you – and if we don't have one, we'll tailor-make one! From the main sights to remote villages, our locally based Travel Specialists will give you unique insights into every place you visit and let you delve into known destinations from new perspectives.

Our tours offer a variety of hotel and resort options, premium stays in deluxe accommodation, heritage hotels, a five-star boutique or on the water in a junk. Tap into our experience let us create an experience unique to you – and one you will never forget.

What type of Holiday to Asia?

Our itineraries at Lanternpath Journeys are created according to different inspirations. Some travelers are interested in the History & Culture of a destination, while some like to stay active with Adventure tours. A Cross Border trip explores different countries in a single tour, while Velvet Summit tours offer the highest level of exclusivity across our destinations. There are 14 different Holiday Types to choose from, or you can mix and match ideas to create your dream vacation.

Target Market(s)

Slightly more female, aged 30-65, are creative, professional and looking for something different, something a bit unusual.

Industry/Entity Type

Boutique

Requirements
Must have
• 5 page designs:

1. Homepage
2. Tours list page for a country
3. Tour page
4. 'Be Inspired' page
5. Country page
6. Enquiry page

Our inspirations.

The following list shows websites we love and which inspire us... to give you some indication of our preferred styles, functions and layouts:

http://www.frostmeridian.example/en/ (we really like this, great personality, like the use of icons for tour types)
http://www.pebblewalks.example.uk/ (very simple design elements and layout)
http://www.sunvalecoast.example/ (great use of background image, nice simple nav bar)
http://www.roamcedarfall.example/ (we like because it has distinct personality and is well suited to the destination)
http://www.seemarlowton.example/ (clear personality through font use)
http://www.vastroving.example/ (original, unique)
http://www.wanderquill.example/long-loop-of-asia (like the map style)

Key design points:

1. You must use our existing logo (attached), but you can change the color scheme of the logo to accord with the whichever color scheme you choose for the main designs.
2. Our logo strapline is "Asia is our Lanternpath" and should be used prominently on the page to reinforce the meaning of our company name.
3. Home page and tours list pages should allow the user to see the choice of tours immediately without scrolling & Introduction copy should be minimal.
4. We and our site visitors are inspired and excited by our photography, this is an element of the site which we would like to maintain and build on, though the section page header sliders are currently too big and do not allow quick access to the section content. This is a design problem which needs a solution. Full page photographic backgrounds may be an answer?
5. Tour page should display other contextual tours, from the same country or style/type
6. We should promote press coverage in various places
7. We should display consultant profiles in various places
8. Map designs for tour page and country page, plus a modal pop out for the home page. These are complex and may have a few small photos and short descriptive text only, though this is limited by your own creativity. We will use graphics and html5/css3 so there are no creative limitations.
9. The 'Inspirations' / 'Be Inspired' page is for people who want travel and holiday ideas, who are looking for inspiration on where to go and what to do. This section needs to reflect the exotic, the unusual, the extraordinary in our destinations and tours, and we leave this to your creative genius to develop. We are also interested in how this inspirations page is related to the blog and social media content we produce daily, is there an integration here? Can we present YouTube videos, our blog posts, Facebook posts etc, on this page? This is another design challenge.
10. We would like to see designs for the tours list page which feature AJAX content filtering (for instance: http://demo.layoutbrisk.example/?acn), we would like to see how to include this type of content filtering on homepage and destination page also.
11. The 'Enquiry' call to action should be on all pages and prominent.
12. The enquiry page can reflect the same fields as the existing website enquiry page

Values to be communicated:

- Exotic: Asia is exotic, and our tours will expose clients to extraordinary sights and unusual cultural encounters.
- Authentic: Our travel consultants all live in the destinations themselves, they are local nationals and have all the insider knowledge to give clients a truly authentic experience of our destinations
- Unique: All of our tours are tailor made, there are no fixed departure dates or join-in groups. All tour itineraries can be uniquely designed for our clients, from departure dates to destinations.
- Trust: Some travelers prefer to book their holidays with local agencies they can meet in person, rather than with online companies like us who live in the destinations and who they only get to meet on Skype video or phone. We want to convey that we are trustworthy. We have attempted this through presenting a 'meet the team' page and a 'press' page and advert, as well as offering a prominent international phone number. How we you build on this and further convey this value?

```html
<!DOCTYPE html>
<html lang="en">
<head>
<meta charset="utf-8">
<title>Lanternpath Journeys – Asia is our Lanternpath</title>
<link href="https://fonts.googleapis.com/css2?family=Arimo:wght@400;700&display=swap" rel="stylesheet">
<style>
:root{
  --blue:#1a8bc3;
  --blue-dark:#1274a6;
  --green:#7dc11e;
  --green-dark:#68a812;
  --nav:#262626;
  --text:#555;
  --muted:#8a8a8a;
  --footer:#474747;
  --footer-bar:#383838;
  --panel:#f4f4f4;
}
*{box-sizing:border-box;margin:0;padding:0}
html,body{width:1028px;height:1200px;overflow:hidden}
body{font-family:"Arimo",Arial,sans-serif;color:var(--text);background:#fff;position:relative}
.abs{position:absolute}
.hero{left:0;top:0;width:1028px;height:529px;background:linear-gradient(180deg,#3d86b8 0%,#5fa6cf 30%,#6f9db3 55%,#5d6f78 80%,#6b5a4c 100%)}
.site-header{left:0;top:0;width:1028px;height:91px}
.brand{left:171px;top:14px;display:flex;align-items:center;gap:10px}
.brand-mark{width:70px;height:66px;border:3px solid #2c3a40;border-radius:10px;background:#c9e2df}
.brand-name{color:#fff;font-size:23px;font-weight:700;line-height:1}
.brand-strap{color:#fff;font-size:10px;margin-top:4px;text-align:right}
.btn-login{left:734px;top:12px;width:60px;height:24px;background:var(--green);color:#fff;font-size:11px;text-align:center;line-height:24px;border-radius:2px}
.btn-signup{left:798px;top:12px;width:59px;height:24px;background:#555;color:#fff;font-size:11px;text-align:center;line-height:24px;border-radius:2px}
.site-search{left:682px;top:42px;width:175px;height:26px;background:#cfdcdc;border:1px solid #b6c4c4;border-radius:2px;font-size:8px;color:#7a8a8a;padding:8px 6px}
.site-search svg{position:absolute;right:6px;top:4px}
.main-nav{left:0;top:91px;width:1028px;height:33px;background:var(--nav);opacity:.95}
.main-nav ul{list-style:none;position:absolute;left:171px;top:0;display:flex;height:33px}
.main-nav li{font-size:11px;color:#9a9a9a;text-transform:uppercase;line-height:33px;padding:0 19px;border-left:1px solid #444}
.main-nav li:first-child{padding-left:0;border-left:0;color:#fff;padding-right:19px}
.finder{left:214px;top:438px;width:601px;height:91px;background:linear-gradient(#fafafa,#e9e9e9)}
.finder-tabs{height:27px;background:var(--blue);display:flex}
.finder-tabs span{font-size:12px;color:#fff;padding:0 10px;line-height:27px}
.finder-tabs .active{background:#fff;color:var(--blue)}
.field{position:absolute;top:41px;width:159px}
.field label{font-size:8px;color:#444;display:block;margin-bottom:4px}
.select{height:20px;background:var(--blue);color:#fff;font-size:8px;line-height:20px;padding-left:6px;position:relative;border-radius:1px}
.select::after{content:"";position:absolute;right:8px;top:7px;border:4px solid transparent;border-top:6px solid #fff}
.finder-go{left:529px;top:56px;width:61px;height:20px;background:var(--green);color:#fff;font-size:11px;text-align:center;line-height:20px;border-radius:2px}
.intro h1{font-size:29px;font-weight:400;color:#8cc63f;letter-spacing:-.5px;position:absolute;left:171px;top:551px;white-space:nowrap}
.intro p{position:absolute;left:171px;top:588px;width:485px;font-size:8px;line-height:13.6px;color:#666}
.enquiry{left:671px;top:556px;width:186px;height:110px}
.enquiry-top{height:68px;background:linear-gradient(#2aa3dd,var(--blue));position:relative}
.agent{position:absolute;left:0;top:0;width:52px;height:68px;background:linear-gradient(#bcd9e8,#e8eef2)}
.enquiry-top .cta{position:absolute;left:58px;top:16px;color:#fff;font-size:11.5px;line-height:14px}
.enquiry-top .toll{position:absolute;right:6px;top:48px;color:#fff;font-size:7.5px}
.enquiry-bottom{height:42px;background:var(--green);color:#fff;text-align:center;padding-top:7px}
.enquiry-bottom small{font-size:8.5px;display:block}
.enquiry-bottom strong{font-size:20px;font-weight:400;display:block;line-height:22px}
.rule{left:171px;top:686px;width:686px;height:1px;background:#ccc}
.card{top:707px;width:218px;height:237px;background:linear-gradient(#fff,#f0f0f0);border-bottom:3px solid #ddd}
.card-title{position:absolute;left:0;top:5px;height:26px;line-height:26px;font-size:12px;color:#fff;padding:0 16px;text-transform:uppercase}
.t-blue{background:var(--blue)} .t-dark{background:#3a3a3a} .t-green{background:var(--green)}
.promo-row{position:absolute;left:4px;width:210px;border-bottom:1px solid #ddd;font-size:10px}
.promo-row .k{position:absolute;left:7px;color:var(--blue)}
.promo-row .v{position:absolute;left:107px;color:var(--blue)}
.promo-row .sub{display:block;font-size:7.5px;color:#999;line-height:10px}
.promo-note{position:absolute;left:11px;top:150px;width:200px;font-size:7.5px;line-height:10px;color:#999}
.link-view{position:absolute;left:86px;top:206px;font-size:8px;color:var(--blue);text-decoration:underline}
.btn-blue{position:absolute;left:130px;top:200px;width:73px;height:24px;background:var(--blue);color:#fff;font-size:8px;line-height:24px;text-align:center;border-radius:2px}
.photo{position:absolute}
.caption{position:absolute;font-size:8px;color:#444;text-transform:uppercase}
.pager{position:absolute;top:207px;width:14px;height:14px;background:#444;border-radius:2px}
.btn-green{position:absolute;left:138px;top:202px;width:61px;height:24px;background:var(--green);color:#fff;font-size:8px;line-height:24px;text-align:center;border-radius:2px}
.site-footer{left:0;top:971px;width:1028px;height:191px;background:var(--footer)}
.foot-col{position:absolute;top:12px}
.foot-col h3{font-size:11.5px;font-weight:400;color:#fff;margin-bottom:14px;text-transform:uppercase}
.foot-col li{list-style:none;font-size:8px;color:#aaa;line-height:15.2px}
.foot-col p{font-size:7.5px;color:#aaa;line-height:10.5px;width:205px}
.newsletter{position:absolute;top:72px;left:0;width:205px;height:25px;background:#fff;border:1px solid #ccc;border-radius:2px;font-size:8px;color:#999;padding:7px 5px}
.newsletter span{position:absolute;right:0;top:0;width:61px;height:23px;background:var(--blue);color:#fff;text-align:center;line-height:23px;font-size:9px}
.footer-bar{left:0;top:1162px;width:1028px;height:38px;background:var(--footer-bar);font-size:8px;color:#aaa;text-align:center;line-height:38px}
</style>
</head>
<body>
<div class="abs hero" role="img" aria-label="Photo of a waterfront Asian city skyline with harbour boats, overlaid with a dark world map marking Asian destinations"></div>

<header class="abs site-header">
  <div class="abs brand">
    <div class="brand-mark"></div>
    <div><div class="brand-name">Lanternpath Journeys</div><div class="brand-strap">Asia is our Lanternpath</div></div>
  </div>
  <div class="abs btn-login">Login</div>
  <div class="abs btn-signup">Sign Up</div>
  <div class="abs site-search">Search
    <svg width="20" height="18" viewBox="0 0 20 18"><circle cx="8" cy="7.5" r="5.5" fill="none" stroke="#111" stroke-width="2.2"/><line x1="12" y1="11.5" x2="17.5" y2="16.5" stroke="#111" stroke-width="3" stroke-linecap="round"/></svg>
  </div>
</header>

<nav class="abs main-nav">
  <ul>
    <li>Home</li><li>Tours List Page for a Country</li><li>Tour Page</li><li>Be Inspired</li><li>Country Page</li><li>Enquiry Page</li>
  </ul>
</nav>

<section class="abs finder">
  <div class="finder-tabs"><span class="active">TOURS</span><span>HOTELS</span></div>
  <div class="field" style="left:11px"><label>Select a Country:</label><div class="select">All Countries</div></div>
  <div class="field" style="left:183px"><label>Select a City:</label><div class="select">All Cities</div></div>
  <div class="field" style="left:356px"><label>Duration:</label><div class="select">All Durations</div></div>
  <div class="abs finder-go">Search</div>
</section>

<section class="intro">
  <h1>ASIA IS OUR LANTERNPATH</h1>
  <p>No one knows a destination better than someone who lives, works and plays there. That's the foundation of Lanternpath Journeys. Our travel specialists reside in Asia. They live Asia, they breathe Asia. And they're intrigued explorers as much as they are citizens of Bangkok, or Bali, or Luang Prabang.<br>The result is a travel company tailor-made for the person with a taste for veering off the well-trodden path, for the adventurer who wants access to Asia's most spectacular sights, but hidden charms as well, on the road less traveled.<br>Want to explore this Asia? Step into our Lanternpath.</p>
</section>

<aside class="abs enquiry">
  <div class="enquiry-top">
    <div class="agent" role="img" aria-label="Photo of a smiling travel consultant with a headset"></div>
    <div class="cta">CLICK HERE TO SEND<br>AN ENQUIRY &gt;&gt;</div>
    <div class="toll">or cal toll free:</div>
  </div>
  <div class="enquiry-bottom"><small>INTERNATIONAL DIAL CODE</small><strong>+800-555-0142</strong></div>
</aside>

<div class="abs rule"></div>

<section class="abs card" style="left:171px">
  <div class="card-title t-blue">Our Promotions</div>
  <div class="promo-row" style="top:45px;height:32px"><span class="k">Promotions Price</span><span class="v">$ 863 (10% Off)<span class="sub">Price Per Person</span></span></div>
  <div class="promo-row" style="top:77px;height:21px;padding-top:5px"><span class="k">Duration</span><span class="v">4 Days / 3 Nights</span></div>
  <div class="promo-row" style="top:98px;height:46px;padding-top:5px"><span class="k">Fast Fact</span><span class="v" style="color:#999;font-size:7.5px;line-height:10px;width:95px">Delve from into Japan cultural heart explore kyoto from an insiders prespective.</span></div>
  <div class="promo-note">Enjoy the cultural soul of Japan with a step back in time to Japan rich, traditional past with a tailored to kyoto, visitng some of Japans most stunning architecture.</div>
  <div class="promo-row" style="top:194px;height:0"></div>
  <span class="link-view">View Tour</span>
  <span class="btn-blue">Send an Inquiry</span>
</section>

<section class="abs card" style="left:405px">
  <div class="card-title t-dark">Hot Destination</div>
  <div class="photo" role="img" aria-label="Photo of tall sandstone pillars covered in forest under a pale sky" style="left:12px;top:46px;width:197px;height:128px;background:linear-gradient(#c9d6dc,#8d9a86 45%,#4f6b45)"></div>
  <div class="caption" style="left:30px;top:189px">Natural wonders of Hunan provi...</div>
  <div class="pager" style="left:94px"></div><div class="pager" style="left:113px"></div>
  <svg class="abs" style="left:94px;top:207px" width="33" height="14"><path d="M9 3 5 7l4 4M24 3l4 4-4 4" fill="none" stroke="#fff" stroke-width="1.4"/></svg>
</section>

<section class="abs card" style="left:639px">
  <div class="card-title t-green" style="padding:0 10px">Why Lanternpath Journeys</div>
  <div class="photo" role="img" aria-label="Photo of a harbour city skyline lit up at dusk" style="left:13px;top:46px;width:196px;height:111px;background:linear-gradient(#2e4f9a,#4d6bb6 45%,#1f2c58)"></div>
  <div class="caption" style="left:15px;top:169px;width:190px;font-size:7.5px;line-height:10px">A travel company that's owned and operated bywho live, work and play in Asia....</div>
  <span class="btn-green">Read more</span>
</section>

<footer class="abs site-footer">
  <div class="foot-col" style="left:171px"><h3>Quick Links</h3><ul><li>Home</li><li>Destinations</li><li>Tours</li><li>Holiday types</li><li>Best value</li><li>About us</li><li>Blog</li></ul></div>
  <div class="foot-col" style="left:299px"><h3>Our Lanternpath</h3><ul><li>Thailand</li><li>Indonesia</li><li>Jaos</li><li>Cambodia</li><li>Japan</li><li>Myanmar</li><li>Vietnam</li><li>China</li><li>Multi-country</li></ul></div>
  <div class="foot-col" style="left:445px"><h3>About Lanternpath Journeys</h3><ul><li>Why book with us</li><li>About us</li><li>Meet the team</li><li>Careers</li><li>In the press</li><li>Affiliate Program</li></ul></div>
  <div class="foot-col" style="left:652px"><h3>Subscribe to our e-newsletter</h3>
    <p>Sign up for Lanternpath Journeys's e-newsletter featuring promotions, travel musings and insider destination.</p>
    <div class="newsletter">Enter your email...<span>Subscribe</span></div>
  </div>
</footer>
<div class="abs footer-bar">© 2013 Lanternpath Journeys. All Rights Reserved. &nbsp;Terms &nbsp;| &nbsp;Contact</div>
</body>
</html>
```